Fast Growing Personal Injury Law Firm Needs Business Card Design

We need a business card design for a fast growing personal injury law firm in Florida. Our name is Dorian Halvorsk, P.A. Our practice is comprised of younger attorneys (in their 30s) that employ more modern techniques/tools than our older competition. We would prefer a look that is a modern play on a classic look. Also, we would like to continue using a color scheme that employs navy blue and kelly green (other shades of green could be fine too) as well as our "E" logo.

Industry/Entity Type

Law Firm

```html
<!DOCTYPE html>
<html lang="en">
<head>
<meta charset="utf-8">
<title>Dorian Halvorsk, P.A. — Business Card</title>
<link rel="stylesheet" href="https://fonts.googleapis.com/css2?family=Libre+Baskerville:wght@400;700&display=swap">
<style>
  :root {
    --navy: #283a8c;
    --green: #1f9a4a;
    --ink: #4a4a52;
    --paper: #ffffff;
    --backdrop: #e9e6e0;
  }
  * { box-sizing: border-box; margin: 0; padding: 0; }
  html, body { width: 1200px; height: 899px; overflow: hidden; }
  body {
    background: var(--backdrop);
    font-family: "Libre Baskerville", Georgia, serif;
    position: relative;
  }
  .card {
    position: absolute;
    background: var(--paper);
    box-shadow: 0 4px 14px rgba(0,0,0,0.14);
    overflow: hidden;
  }
  /* front */
  .card-front { left: 70px; top: 300px; width: 520px; height: 298px; }
  .front-lockup {
    position: absolute; left: 64px; top: 112px;
    display: flex; align-items: center; gap: 14px;
  }
  .mark-square { width: 46px; height: 46px; background: var(--navy); flex: none; }
  .front-name { color: var(--navy); font-weight: 700; font-size: 25px; line-height: 1.1; }
  .front-tagline { color: var(--green); font-weight: 700; font-size: 20px; line-height: 1.15; letter-spacing: 0.5px; }

  /* back */
  .card-back { left: 660px; top: 190px; width: 298px; height: 520px; }
  .back-brand {
    position: absolute; top: 40px; left: 0; right: 0;
    display: flex; justify-content: center; align-items: center; gap: 9px;
  }
  .back-brand .mark-square { width: 22px; height: 22px; }
  .back-brand-name { color: var(--navy); font-size: 17px; }
  .back-name {
    position: absolute; top: 110px; width: 100%; text-align: center;
    color: var(--navy); font-size: 22px; letter-spacing: 0.5px;
  }
  .back-role {
    position: absolute; top: 142px; width: 100%; text-align: center;
    color: var(--ink); font-size: 13px; font-style: italic;
  }
  .divider { position: absolute; top: 185px; left: 34px; width: 230px; height: 20px; }
  .contact {
    position: absolute; top: 218px; left: 34px; right: 20px;
    color: var(--ink); font-size: 11.5px; line-height: 1.65;
  }
  .contact .address { margin-bottom: 12px; }
  .banner { position: absolute; left: 0; bottom: 0; width: 298px; height: 96px; }
  .banner-text {
    position: absolute; left: 20px; bottom: 18px;
  }
  .banner-name { color: var(--navy); font-size: 15px; }
  .banner-tagline { color: #ffffff; font-size: 11px; margin-top: 4px; }
</style>
</head>
<body>

  <section class="card card-front">
    <div class="front-lockup">
      <span class="mark-square"></span>
      <div>
        <div class="front-name">Dorian Halvorsk, P.A.</div>
        <div class="front-tagline">Personal Injury Attorneys</div>
      </div>
    </div>
  </section>

  <section class="card card-back">
    <div class="back-brand">
      <span class="mark-square"></span>
      <span class="back-brand-name">Halvorsk</span>
    </div>
    <div class="back-name">Dorian Halvorsk</div>
    <div class="back-role">Attorney at Law</div>

    <svg class="divider" viewBox="0 0 230 20" aria-hidden="true">
      <line x1="0" y1="10" x2="100" y2="10" stroke="#283a8c" stroke-width="1"/>
      <line x1="130" y1="10" x2="230" y2="10" stroke="#283a8c" stroke-width="1"/>
      <path d="M115 17 C110 11 109 8 109 7 A6 6 0 0 1 121 7 C121 8 120 11 115 17 Z" fill="none" stroke="#283a8c" stroke-width="1.4"/>
      <circle cx="115" cy="7" r="1.8" fill="#283a8c"/>
    </svg>

    <div class="contact">
      <div class="address">2150 Harbor Point Drive, Suite 210<br>Palmetto Bay, Florida 33157</div>
      <div>P: (555) 214-3380</div>
      <div>F: (555) 214-3381</div>
      <div>E: dorian@halvorsklaw.com</div>
      <div>Web: halvorsklaw.com</div>
    </div>

    <svg class="banner" viewBox="0 0 298 96" aria-hidden="true">
      <path d="M0 8 H230 L266 52 L230 96 H0 Z" fill="#1f9a4a" stroke="#283a8c" stroke-width="2"/>
    </svg>
    <div class="banner-text">
      <div class="banner-name">Dorian Halvorsk, P.A.</div>
      <div class="banner-tagline">Personal Injury Attorneys</div>
    </div>
  </section>

</body>
</html>
```